Corporate Design für Halle 24
Hallo,
wir werden in naher Zukunft ein Onlineshop sein, der sich mit dem Verkauf von Bodenbelägen ( Parkett, Laminat, Vinyl, Massivholzdielen, Terrassendielen, Kork sowie Gartenmöbel und Grills ) beschäftigt.
Der Verkauf erfolgt rein über den Shop.
Der Kunde kann im Shop direkt bestellen, kann aber auch die Hotline anrufen und sich beraten lassen. Hier kann der Berater paralell ein Angebot erstellen.
Unser Geschäftskonzept geht in Richtung Moderne, Loftstyle, Jugendlich, wertig jedoch nicht zu teuer, dementsprechend sagt es der Name schon aus.
Unsere Zielgruppe sollte bei ca.25- 60 Jahren Liegen und ansprechend sein, kann natürlich auch jünger oder älter sein.
Aufgabenstellung
Design das hängen bleibt!
Uns gefällt die Idee der Darstellung in der Art, dass die 11 im Buchstaben O steht
Die Idee ist das wir das O mit der Zahl als favicon nehmen und sich als Symbol einprägen sollte.
Frische neutrale Farben
Helle Seiten im Web, helles Auftreten auf Visitenkarten und Briefpapier.

```html
<!DOCTYPE html>
<html lang="de">
<head>
<meta charset="utf-8">
<title>Halle 24 – Geschäftsausstattung</title>
<link href="https://fonts.googleapis.com/css2?family=Montserrat:wght@500;600;700;800&family=Open+Sans:wght@400;600;700&family=Allura&display=swap" rel="stylesheet">
<style>
  :root {
    --bronze: #a5896a;
    --ink: #1f1f1f;
    --paper: #ffffff;
    --stage: #323336;
    --muted: #555;
  }
  * { box-sizing: border-box; margin: 0; padding: 0; }
  html, body { width: 1200px; height: 974px; overflow: hidden; background: var(--paper); }
  body { position: relative; font-family: "Open Sans", sans-serif; color: var(--ink); }

  .wordmark {
    font-family: "Montserrat", sans-serif;
    font-weight: 800;
    color: var(--bronze);
    letter-spacing: 0.02em;
    white-space: nowrap;
    line-height: 1;
  }
  .hero-mark { position: absolute; top: 96px; left: 0; width: 1200px; text-align: center; font-size: 44px; }

  .stage { position: absolute; left: 37px; top: 219px; width: 1126px; height: 718px; background: var(--stage); }

  .sheet { position: absolute; background: var(--paper); overflow: hidden; box-shadow: 0 6px 14px rgba(0,0,0,.45); }

  /* Letterhead */
  .letterhead { left: 135px; top: 66px; width: 416px; height: 588px; }
  .letterhead .wordmark { position: absolute; right: 30px; top: 31px; font-size: 23px; }
  .sender-line { position: absolute; left: 45px; top: 90px; font-size: 4.6px; color: var(--bronze); font-weight: 600; border-bottom: 0.8px solid var(--bronze); padding-bottom: 1px; }
  .recipient { position: absolute; left: 45px; top: 107px; font-size: 6.4px; line-height: 8.4px; }
  .recipient .city { margin-top: 8px; }
  .subject { position: absolute; left: 45px; top: 200px; font-size: 6.4px; font-weight: 700; }
  .body-copy { position: absolute; left: 45px; top: 222px; width: 228px; font-size: 5.6px; line-height: 7.5px; color: #333; }
  .body-copy p + p { margin-top: 7.5px; }
  .closing { position: absolute; left: 45px; top: 420px; font-size: 5.6px; color: #333; }
  .signature { position: absolute; left: 45px; top: 436px; font-family: "Allura", cursive; font-size: 21px; color: var(--ink); }
  .footer-rule { position: absolute; left: 45px; top: 538px; width: 248px; height: 1px; background: var(--bronze); }
  .footer { position: absolute; top: 546px; font-family: "Montserrat", sans-serif; font-size: 4.4px; line-height: 7px; font-weight: 700; text-transform: uppercase; }
  .footer.col-company { left: 45px; }
  .footer.col-contact { left: 136px; }
  .footer.col-bank { left: 228px; }
  .icon { display: inline-block; width: 5px; height: 5px; border-radius: 50%; background: var(--bronze); vertical-align: -0.8px; margin-right: 2px; }
  .corner-disc { position: absolute; border-radius: 50%; background: var(--bronze); }
  .letterhead .corner-disc { width: 80px; height: 80px; left: 338px; top: 525px; }

  /* Business cards */
  .card { left: 724px; width: 252px; height: 163px; }
  .card-front { top: 158px; }
  .card-back { top: 398px; background: var(--bronze); display: flex; align-items: center; justify-content: center; }
  .card-front .wordmark { position: absolute; left: 22px; top: 22px; font-size: 25px; }
  .card-back .wordmark { color: var(--paper); font-size: 30px; }
  .card-info { position: absolute; left: 23px; font-family: "Montserrat", sans-serif; font-weight: 700; text-transform: uppercase; font-size: 6.2px; line-height: 8.4px; }
  .card-info .role { color: var(--bronze); }
  .card-name { top: 60px; }
  .card-address { top: 83px; }
  .card-contact { top: 107px; }
  .card-web { top: 132px; color: var(--bronze); letter-spacing: .06em; }
  .card-front .corner-disc { width: 72px; height: 72px; left: 183px; top: 107px; }
</style>
</head>
<body>
  <div class="wordmark hero-mark">HALLE 24</div>

  <section class="stage">
    <article class="sheet letterhead">
      <div class="wordmark">HALLE 24</div>
      <div class="sender-line">Vorname Nachname, Musterstr. 123, 12345 Musterstadt</div>
      <div class="recipient">
        <div>Martina Musterfrau</div>
        <div>Musterstraße 456</div>
        <div class="city">12345 Berlin</div>
      </div>
      <div class="subject">Quidero molore, atatur sae. Nequat,</div>
      <div class="body-copy">
        <p>Ur sit, imus, ipicatem voluptate eum re dolluptios sequosam, eum reritati am volor sapedissi quo blaboribust, sequass itasped igendi cus exerfer feruptas iusanda ndaest, qui omnis nus aut fugitinis quatur ad ullaut mostem quasperiae corem et aciatem illatin ciduntores quidis utemquam autemperae soluptiae lab illacescia solorum et fugiam ratatatus exerro blaciis samusam etur? Uga. Neque nam simi, nest, ommod essedios magnatia nossi aute nonsequam fugiaspis moluptas sed el int etur saepe nonsecatem excea noneceperrum ulligendit faccullores et lantur si ium at.Ota cuptae non ea de opta voles rem rae dolore ilia vellab isi blanis idit veribus auda alit labore desenis imenis que in con rehent, explat ped que volorum, autent, si tetur?</p>
        <p>Ihil ium restior ecepero reptistius es aborepe diatiunt dignis diciae voluptu ribearit, que nat aute et as maximus, qui blab iur aut volest, nonsequae odios doluptatiae velignimin perescia vent. Pa voluptas expero corectur molest eaquid enda vidus verciis quodi te dit aliquid unturem poreper feratur? Quis aut rehenihilit et quam, eris et perorru mquamusa quo et untia volupie nisimoluptae esseribus cora doluptati doluptatur atisciumqui re pa quat aut lam solescia intiis et millabor sit odis et quos re sam, vendicientur abo. Equi totatus rest, nosam quodi omni doloriosam des ea nimpelique volo elendae dellign ihilitis solupta temporp orupta iuntia ipiste natibusapis volesedis reriori taerrup tatiberes nobitiur, sequi omnihillab id maximagnat omnimus dolo quunt, int aut earum lacit peliquunt iduciet, id que autemolum deruptati te non re.</p>
      </div>
      <div class="closing">Sincerely</div>
      <div class="signature">M. Mmann</div>
      <div class="footer-rule"></div>
      <div class="footer col-company">Musterfirma GmbH<br>Musterstr. 123<br>12345 Musterstadt</div>
      <div class="footer col-contact"><span class="icon"></span>010 / 234 567 89<br><span class="icon"></span>010 / 234 567 90<br><span class="icon"></span>info@musterweb.de</div>
      <div class="footer col-bank">Musterbank AG<br>IBAN: DE12 3456 7890 1234<br>BIC: ABC456789</div>
      <div class="corner-disc"></div>
    </article>

    <article class="sheet card card-front">
      <div class="wordmark">HALLE 24</div>
      <div class="card-info card-name">Vorname Nachname<br><span class="role">Geschäftsführung</span></div>
      <div class="card-info card-address">Musterfirma GmbH<br>Musterstr. 123 &nbsp;•&nbsp; 12345 Musterstadt</div>
      <div class="card-info card-contact"><span class="icon"></span>010 / 234 567 89<br><span class="icon"></span>010 / 234 567 90<br><span class="icon"></span>info@musterweb.de</div>
      <div class="card-info card-web">www.musterweb.de</div>
      <div class="corner-disc"></div>
    </article>

    <article class="sheet card card-back">
      <div class="wordmark">HALLE 24</div>
    </article>
  </section>
</body>
</html>
```